Animal Eye Clinic needs a Business card

We are a new veterinary ophthalmology practice (Tessaly Animal Eye Care) and we need a business card designed. We only see animal eyes - we are not a regular veterinary clinic. We already have a logo. We are looking for a professional, good looking business card to hand out to our clients. We are looking for something simple but professional and contemporary. Our logo is likely the only picture/graphic that needs to be on the card.
Updates

Contact Information for Business Card

Marisol Dunkley, BSc, DVM, MSc, DipACVO
Veterinary Ophthalmologist

Phone: 250.418.3097
Email: tessalyanimaleyecare@mailbrook.net
Website: tessalyanimaleyecare.net
Address: 1840 Pellworth Rd
Brackenridge, NS, V4T 8M3

Colors

Designer to choose colors to be used in the design.

Requirements
Must have
• Our logo (attached)

```html
<!DOCTYPE html>
<html lang="en">
<head>
<meta charset="utf-8">
<title>Tessaly Animal Eye Care — Business Card</title>
<link rel="stylesheet" href="https://fonts.googleapis.com/css2?family=Roboto:wght@300;400;500;700&display=swap">
<style>
  :root {
    --page: #e9e7e4;
    --card: #2f3033;
    --teal: #1a98a6;
    --ink: #f1f1f1;
    --rule: #bfc2c4;
  }
  * { box-sizing: border-box; margin: 0; padding: 0; }
  html, body {
    width: 1200px; height: 716px; overflow: hidden;
    background: var(--page);
    font-family: "Roboto", Arial, sans-serif;
  }
  .sheet {
    position: relative; width: 1200px; height: 716px;
    display: flex; align-items: center; justify-content: center; gap: 60px;
  }
  .card {
    position: relative; width: 520px; height: 297px;
    background: var(--card);
    border-bottom: 4px solid var(--teal);
    border-left: 2px solid var(--teal);
    box-shadow: 0 10px 28px rgba(0,0,0,.25);
  }
  .brand {
    display: flex; align-items: center; gap: 10px;
    color: var(--teal); font-weight: 700; text-transform: uppercase;
    letter-spacing: .02em; white-space: nowrap;
  }
  .brand-dot { border-radius: 50%; background: var(--teal); flex: none; }

  .card-front .brand {
    position: absolute; left: 50%; top: 50%; transform: translate(-50%, -50%);
    font-size: 24px;
  }
  .card-front .brand-dot { width: 34px; height: 34px; }

  .card-back .brand { position: absolute; right: 28px; top: 50px; font-size: 15px; }
  .card-back .brand-dot { width: 24px; height: 24px; }

  .person { position: absolute; left: 32px; top: 108px; }
  .person-name { color: var(--teal); font-weight: 700; font-size: 14px; }
  .person-title { color: var(--ink); font-weight: 300; font-size: 12.5px; margin-top: 3px; }
  .divider {
    position: absolute; left: 32px; right: 40px; top: 154px;
    height: 1px; background: var(--rule);
  }
  .contacts {
    position: absolute; left: 32px; top: 168px;
    list-style: none; color: var(--ink); font-weight: 300; font-size: 12px; line-height: 1.55;
  }
  .contacts li { display: flex; align-items: center; gap: 7px; }
  .contacts svg { width: 10px; height: 10px; fill: var(--teal); flex: none; }
  .contacts .accent { color: var(--teal); }
  .address {
    position: absolute; right: 40px; bottom: 20px;
    color: var(--ink); font-weight: 300; font-size: 13px; line-height: 1.4;
    font-style: normal; text-align: left;
  }
</style>
</head>
<body>
<main class="sheet">
  <section class="card card-front" aria-label="Card front">
    <div class="brand"><span class="brand-dot"></span>Tessaly Animal Eye Care</div>
  </section>

  <section class="card card-back" aria-label="Card back">
    <div class="brand"><span class="brand-dot"></span>Tessaly Animal Eye Care</div>

    <div class="person">
      <p class="person-name">Marisol Dunkley, BSc, DVM, MSc, DipACVO</p>
      <p class="person-title">Veterinary Ophthalmologist</p>
    </div>
    <div class="divider"></div>

    <ul class="contacts">
      <li>
        <svg viewBox="0 0 10 10"><path d="M2 0.5 L3.6 2.8 L2.7 3.8 C3.3 5.2 4.8 6.7 6.2 7.3 L7.2 6.4 L9.5 8 L8.5 9.5 C4.5 9.5 0.5 5.5 0.5 1.5 Z"/></svg>
        250.418.3097
      </li>
      <li>
        <svg viewBox="0 0 10 10"><path d="M0.5 2 H9.5 V8.5 H0.5 Z M1 2.5 L5 5.5 L9 2.5" stroke="#2f3033" stroke-width=".8"/></svg>
        tessalyanimaleyecare@mailbrook.net
      </li>
      <li>
        <svg viewBox="0 0 10 10"><circle cx="5" cy="5" r="4.5"/><path d="M0.5 5 H9.5 M5 0.5 C3 3 3 7 5 9.5 M5 0.5 C7 3 7 7 5 9.5" stroke="#2f3033" stroke-width=".7" fill="none"/></svg>
        <span>www.<span class="accent">tessalyanimaleyecare</span>.net</span>
      </li>
    </ul>

    <address class="address">
      1840 Pellworth Rd<br>
      Brackenridge, NS, V4T 8M3
    </address>
  </section>
</main>
</body>
</html>
```